11 x 17 Thelanoros Quote

Design the following quote in a poster.

"First say to yourself what you would be; then do what you have to do." - Thelanoros

See here for inspiration - https://prints.quietgrove.com/

Quote

```html
<!DOCTYPE html>
<html lang="en">
<head>
<meta charset="utf-8">
<title>Thelanoros Quote Poster</title>
<link rel="stylesheet" href="https://fonts.googleapis.com/css2?family=Francois+One&family=Open+Sans:wght@700&display=swap">
<style>
  :root {
    --bg-core: #a3100f;
    --bg-mid: #7a0606;
    --bg-edge: #2e0101;
    --quote-ink: #efe4c4;
    --quote-shadow: #e0231f;
    --author-ink: #ffffff;
  }
  html, body {
    margin: 0;
    padding: 0;
    width: 776px;
    height: 1200px;
    overflow: hidden;
    background: var(--bg-edge);
  }
  .poster {
    position: relative;
    width: 776px;
    height: 1200px;
    overflow: hidden;
    background:
      radial-gradient(ellipse 70% 55% at 52% 45%, var(--bg-core) 0%, var(--bg-mid) 55%, var(--bg-edge) 100%);
  }
  .poster__texture {
    position: absolute;
    inset: 0;
    width: 100%;
    height: 100%;
    opacity: 0.35;
    mix-blend-mode: multiply;
  }
  .quote {
    position: absolute;
    left: 0;
    right: 0;
    top: 228px;
    margin: 0 auto;
    width: 776px;
    padding-left: 30px;
    box-sizing: border-box;
    text-align: center;
    font-family: "Francois One", "Oswald", sans-serif;
    font-size: 76px;
    line-height: 93.5px;
    letter-spacing: 1px;
    text-transform: uppercase;
    color: var(--quote-ink);
    text-shadow: 4px 3px 0 var(--quote-shadow);
  }
  .quote__initial {
    font-size: 96px;
  }
  .author {
    position: absolute;
    left: 0;
    right: 0;
    top: 922px;
    margin: 0;
    padding-left: 30px;
    text-align: center;
    font-family: "Open Sans", "Arial", sans-serif;
    font-weight: 700;
    font-size: 33px;
    color: var(--author-ink);
  }
</style>
</head>
<body>
  <main class="poster">
    <svg class="poster__texture" viewBox="0 0 776 1200" preserveAspectRatio="none" aria-hidden="true">
      <filter id="paper-grain">
        <feTurbulence type="fractalNoise" baseFrequency="0.012 0.02" numOctaves="4" seed="7"/>
        <feColorMatrix type="matrix" values="0 0 0 0 0.2  0 0 0 0 0  0 0 0 0 0  0 0 0 -1.4 1.1"/>
      </filter>
      <rect width="776" height="1200" filter="url(#paper-grain)"/>
    </svg>
    <blockquote class="quote">
      "<span class="quote__initial">F</span>irst<br>
      say to yourself<br>
      what you<br>
      would be<br>
      then do<br>
      what you<br>
      have to do."
    </blockquote>
    <p class="author">Thelanoros</p>
  </main>
</body>
</html>
```